Flyer to advertise gutter cleaning throughout the Autumn and winter monthss

I need a new flyer to advertise gutter and driveway cleaning, roof and gutter repairs.

I am an experienced licensed Plumber and Gasfitter looking to broaden my scope of work to gutter cleaning. I am experienced in cleaning gutter and live in a area with large gum trees. I wont something that's clear, eye catching but not too busy.

Flyer requirements: Free roof inspection - no obligation. Gutter Cleaning from $199. Pictures of men using blower or hands to clean roof gutters (no obvious faces) to be included. Australian looking houses.

A mention that 'All general plumbing maintenance' is offered as other services but not too much wording about this as the target is for gutter cleaning.

Phone number: 0427 386 915 (in this format)
Business Name: Bellvane Plumbing & Gasfitting
License: 3174520
ABN: 71904352816
Web: http://bellvaneplumbing.example-site.net/

Target Market(s)

Elderly - busy working class

Industry/Entity Type

Plumber

Font styles to use
Sans Serif

Colors
0355a3
fbed22
ec1f27
f78f20

Requirements
Must have
• Roof Gutter Cleaning pictures
• Men in protective clothing if possible
Nice to have
• More information:
• Prevent against flooding, mold, rust, rotting and corrosion now!
• Gutter Cleaning Services
• • Remove leaves, sticks, and other debris
• • Clear away clogs
• • Test your downpipes
• • Pinpoint any gutter issues
• • Repair gutter
• With regular service, you can count on your property to be well-protected no matter what the forecast!
Should not have
• Houses that don't look Australian

```html
<!DOCTYPE html>
<html lang="en">
<head>
<meta charset="utf-8">
<title>Bellvane Plumbing &amp; Gasfitting – Gutter Cleaning Flyer</title>
<link href="https://fonts.googleapis.com/css2?family=Open+Sans:ital,wght@0,400;0,600;0,700;0,800;1,400;1,600&family=Kaushan+Script&display=swap" rel="stylesheet">
<style>
  :root{
    --navy:#282369;
    --red:#e5093a;
    --red-deep:#d9002b;
    --yellow:#f2e41f;
    --teal:#0d7470;
    --paper:#e9e9e9;
    --ink:#1f1d5c;
    --bg:#d6d6d6;
    --white:#ffffff;
  }
  *{box-sizing:border-box;margin:0;padding:0}
  html,body{width:1200px;height:1000px;overflow:hidden}
  body{background:var(--bg);font-family:"Open Sans",Arial,sans-serif;position:relative}
  .flyer{position:absolute;left:240px;top:35px;width:720px;height:930px;background:var(--paper);overflow:hidden;box-shadow:0 2px 10px rgba(0,0,0,.12)}
  .hero-photo{position:absolute;left:440px;top:0;width:280px;height:565px;
    background:linear-gradient(170deg,#3d4b6a 0%,#6b7898 35%,#55607c 60%,#c9762e 78%,#e7c648 88%,#dadada 100%)}
  .masthead{position:absolute;left:0;top:0;width:440px;height:400px;background:var(--navy)}
  .brand{position:absolute;left:36px;top:48px;display:flex;align-items:center;gap:10px}
  .brand-dot{width:34px;height:34px;border-radius:50%;background:var(--white)}
  .brand-name{color:var(--white);font-weight:700;font-size:13px;letter-spacing:.2px;text-transform:uppercase;line-height:1.15;width:170px}
  .rule{position:absolute;left:36px;top:110px;width:118px;height:4px;background:var(--red)}
  .headline{position:absolute;left:34px;top:138px;color:var(--white);font-weight:800;line-height:.98;text-transform:uppercase}
  .headline .l1{display:block;font-size:70px;letter-spacing:-.5px}
  .headline .l2{display:block;font-size:76px;letter-spacing:-1px}
  .price{position:absolute;left:42px;top:300px;display:flex;align-items:baseline;gap:10px}
  .price .from{font-family:"Kaushan Script",cursive;color:var(--white);font-size:50px}
  .price .amount{font-weight:800;color:var(--yellow);font-size:66px;letter-spacing:-1px}
  .alert-band{position:absolute;left:0;top:400px;width:440px;height:130px;background:linear-gradient(90deg,var(--red-deep),var(--red))}
  .alert-band p{position:absolute;left:42px;top:22px;width:270px;color:var(--white);font-style:italic;font-weight:600;font-size:20px;line-height:1.3}
  .guarantee{position:absolute;left:368px;top:360px;width:176px;height:176px;border-radius:50%;background:var(--teal);border:5px solid var(--white);
    display:flex;flex-direction:column;align-items:center;justify-content:center;gap:4px;color:var(--white);text-align:center;text-transform:uppercase}
  .guarantee .g-top{font-weight:700;font-size:15px;letter-spacing:1px}
  .guarantee .g-main{font-weight:800;font-size:20px;line-height:1}
  .guarantee svg{margin-top:4px}
  .services{position:absolute;left:40px;top:575px;width:360px;color:var(--ink)}
  .services h2{font-weight:800;font-size:21px;text-transform:uppercase;letter-spacing:.2px}
  .services ul{list-style:none;margin-top:8px}
  .services li{display:flex;align-items:center;gap:10px;font-size:15.5px;font-weight:600;color:#1c1c2c;height:26px}
  .services li svg{flex:none}
  .note{position:absolute;left:40px;top:746px;width:300px;font-style:italic;font-size:11.5px;line-height:1.3;color:#1c1c2c}
  .offer{position:absolute;left:0;top:792px;width:440px;text-align:center;color:var(--ink);font-weight:800;font-size:18px;line-height:1.25;text-transform:uppercase}
  .phone{position:absolute;left:0;top:838px;width:440px;text-align:center;color:var(--red-deep);font-weight:800;font-size:38px;letter-spacing:.5px}
  .web{position:absolute;left:0;top:886px;width:440px;text-align:center;color:var(--ink);font-weight:700;font-size:12px}
  .licence{position:absolute;left:0;top:906px;width:440px;text-align:center;color:#777;font-size:10px}
  .strip{position:absolute;left:432px;width:288px;border:5px solid var(--white);border-right:none}
  .strip-one{top:583px;height:128px;background:linear-gradient(100deg,#7a5838 0%,#a77a4e 40%,#8c8680 70%,#6f6c6a 100%)}
  .strip-two{top:724px;height:130px;background:linear-gradient(180deg,#b9b4ae 0%,#8a4b3d 30%,#6f7580 55%,#4c5460 100%)}
  .tagline{position:absolute;left:462px;top:864px;width:258px;height:44px;background:linear-gradient(90deg,#3b3b3b,#222);color:var(--white);font-weight:700;font-size:14px;white-space:nowrap;display:flex;align-items:center;padding-left:16px}
</style>
</head>
<body>
  <main class="flyer">
    <div class="hero-photo" role="img" aria-label="Close-up photo of a roof edge with autumn leaves collected in the gutter"></div>

    <section class="masthead">
      <div class="brand">
        <span class="brand-dot"></span>
        <span class="brand-name">Bellvane Plumbing &amp; Gasfitting</span>
      </div>
      <div class="rule"></div>
      <h1 class="headline"><span class="l1">Gutter</span><span class="l2">Cleaning</span></h1>
      <div class="price"><span class="from">From</span><span class="amount">$199</span></div>
    </section>

    <section class="alert-band">
      <p>Prevent against flooding, mold, rust, rotting and corrosion now!</p>
    </section>

    <div class="guarantee">
      <span class="g-top">All Work</span>
      <span class="g-main">Guaranteed</span>
      <svg width="26" height="20" viewBox="0 0 26 20"><path d="M3 10 L10 17 L23 3" fill="none" stroke="var(--yellow)" stroke-width="4" stroke-linecap="round" stroke-linejoin="round"/></svg>
    </div>

    <section class="services">
      <h2>Gutter Cleaning Services</h2>
      <ul>
        <li><svg width="11" height="10" viewBox="0 0 11 10"><path d="M1 5 L4 8 L10 1" fill="none" stroke="var(--red)" stroke-width="2"/></svg>Remove leaves, sticks, and other debris</li>
        <li><svg width="11" height="10" viewBox="0 0 11 10"><path d="M1 5 L4 8 L10 1" fill="none" stroke="var(--red)" stroke-width="2"/></svg>Clear away clogs</li>
        <li><svg width="11" height="10" viewBox="0 0 11 10"><path d="M1 5 L4 8 L10 1" fill="none" stroke="var(--red)" stroke-width="2"/></svg>Test your downpipes</li>
        <li><svg width="11" height="10" viewBox="0 0 11 10"><path d="M1 5 L4 8 L10 1" fill="none" stroke="var(--red)" stroke-width="2"/></svg>Pinpoint any gutter issues</li>
        <li><svg width="11" height="10" viewBox="0 0 11 10"><path d="M1 5 L4 8 L10 1" fill="none" stroke="var(--red)" stroke-width="2"/></svg>Repair gutter</li>
      </ul>
    </section>
    <p class="note">With regular service, you can count on your property to be well&#8209;protected no matter what the forecast!</p>

    <p class="offer">Free Roof Inspection<br>No Obligation</p>
    <p class="phone">0427 386 915</p>
    <p class="web">bellvaneplumbing.example-site.net</p>
    <p class="licence">License: 3174520 | ABN: 71904352816</p>

    <div class="strip strip-one" role="img" aria-label="Gloved hand scooping dry leaves out of a roof gutter"></div>
    <div class="strip strip-two" role="img" aria-label="Roof gutter line filled with leaf debris along a tiled roof"></div>
    <div class="tagline">All Plumbing &amp; Gasfitting Services</div>
  </main>
</body>
</html>
```